Flyer für Therapie- und Gesundheitsdienstleister
Zielgruppe
Therapie- und Gesundheitsdienstleister im Bereich Physiotherapie, Podologie, Prävention und betriebliche Gesundheitsförderung. Für dieses Projekt möchten wir einen Flyer erstellen lassen für die Bewerbung der betrieblichen Gesundheitsförderungen in bzw. für Firmen
Aufgabenstellung
Klare Strukturen, nicht verspielt, DINA4 oder DINA5; leicht medizinischer Touch, evntuell Stockfotos integrieren, edel und hochwertiges Design

```html
<!DOCTYPE html>
<html lang="de">
<head>
<meta charset="utf-8">
<title>Flyer Betriebliche Gesundheitsförderung</title>
<link href="https://fonts.googleapis.com/css2?family=Montserrat:wght@400;500;600;700&display=swap" rel="stylesheet">
<style>
:root{
  --orange:#ef7d00;
  --ink:#222;
  --grey:#555;
  --dark:#4a4a4a;
  --panel:#efefef;
  --bg:#fff;
}
*{box-sizing:border-box;margin:0;padding:0}
html,body{width:1200px;height:806px;overflow:hidden;background:var(--bg)}
body{font-family:'Montserrat',sans-serif;color:var(--ink);position:relative}
.page{position:absolute;top:39px;width:513px;height:726px;background:#fff;overflow:hidden;box-shadow:0 2px 10px rgba(0,0,0,.18)}
.page--front{left:47px}
.page--back{left:639px}
.abs{position:absolute}
.badge{position:absolute;border-radius:50%;background:var(--orange);color:#fff;font-weight:700;text-align:center;display:flex;align-items:center;justify-content:center;font-size:10.5px;line-height:1.35;box-shadow:0 3px 8px rgba(0,0,0,.25);z-index:2}
.footer-tab{position:absolute;bottom:0;left:178px;width:157px;height:26px;background:var(--dark);border-radius:6px 6px 0 0;color:#fff;font-size:9px;font-weight:700;display:flex;align-items:center;justify-content:center}
/* front */
.front-title{top:364px;left:0;width:100%;text-align:center;color:var(--orange);font-size:18px;font-weight:700;white-space:nowrap}
.front-intro{top:397px;left:30px;width:453px;text-align:center;font-size:12px;line-height:17px;color:var(--grey)}
.front-intro b{color:#333}
.points{top:468px;left:24px;width:204px;height:201px;background:var(--panel);border-radius:6px;box-shadow:0 2px 6px rgba(0,0,0,.15);padding:15px 11px;font-size:8.6px;line-height:12.5px;color:#333}
.point{display:flex;align-items:flex-start;gap:8px;font-weight:600;margin-top:14px}
.point .num{flex:none;width:20px;height:20px;border-radius:50%;background:var(--orange);color:#fff;font-weight:700;font-size:10px;display:flex;align-items:center;justify-content:center}
.point span{padding-top:2px}
.point--single span{padding-top:4px}
.points p.last{margin-top:16px}
.front-text{top:468px;left:247px;width:250px;font-size:8.6px;line-height:12.9px;color:#333;white-space:nowrap}
.front-text p.strong{font-weight:700;color:#111;margin-top:13px}
/* back */
.back-title{top:150px;left:29px;font-size:18px;font-weight:600;color:#333}
.col{position:absolute;top:177px;font-size:8.5px;line-height:12.9px;color:#333;white-space:nowrap}
.col-left{left:30px;width:240px}
.col-right{left:284px;width:215px}
.col h3{color:var(--orange);font-size:10.5px;font-weight:700;margin-bottom:6px}
.col h3.gap{margin-top:12px}
.col ul{list-style:none}
.col li{position:relative;padding-left:11px;margin-bottom:4px}
.col li::before{content:"✓";position:absolute;left:0;top:0;font-size:8px}
.cost{top:535px;left:20px;width:310px;height:146px;background:var(--panel);border-radius:6px;box-shadow:0 2px 6px rgba(0,0,0,.15);padding:9px 12px;font-size:8.3px;line-height:12.9px;color:#333;white-space:nowrap}
.cost h2{font-size:17px;font-weight:600;color:#333;margin-bottom:4px}
.contact{top:536px;left:354px;width:150px;font-size:8.5px;line-height:10.5px;color:#555}
.contact .portrait{width:67px;height:79px;border-radius:4px;background:linear-gradient(#d8d8d8,#c4c4c4)}
.contact .name{font-weight:700;color:#333;margin:9px 0 9px}
.contact p{margin-bottom:5px}
</style>
</head>
<body>

<section class="page page--front">
  <svg class="abs" style="top:0;left:0" width="513" height="340" viewBox="0 0 513 340" role="img" aria-label="Foto: lächelnde Frau mit Brille in grüner Bluse im hellen Büro">
    <defs><linearGradient id="officeTone" x1="0" y1="0" x2="1" y2="1">
      <stop offset="0" stop-color="#c9c4bd"/><stop offset=".45" stop-color="#6f8c84"/><stop offset="1" stop-color="#2c7a6b"/>
    </linearGradient></defs>
    <path d="M0 0H513V248Q420 330 250 339Q100 340 0 300Z" fill="url(#officeTone)"/>
  </svg>
  <div class="badge" style="left:375px;top:238px;width:98px;height:98px">Jetzt einen<br>persönlichen<br>Termin<br>vereinbaren!</div>

  <h1 class="abs front-title">Betriebliche Gesundheitsförderung</h1>
  <p class="abs front-intro">Die betriebliche Gesundheitsförderung hat das Ziel die <b>Gesundheit der<br>Mitarbeiter</b> zu erhalten und zu fördern sowie die <b>Leistungsfähigkeit und<br>Motivation</b> der Belegschaft zu steigern.</p>

  <div class="abs points">
    <p>Immer mehr gewinnen jedoch<br>folgende Punkte an Bedeutung für<br>Unternehmen:</p>
    <div class="point point--single"><div class="num">1.</div><span>Mitarbeiterbindung &amp;</span></div>
    <div class="point"><div class="num">2.</div><span>Arbeitgeber Attraktivität zu<br>erhöhen, um ein Vorteil am<br>Bewerbermarkt zu erzielen.</span></div>
    <p class="last">Auch da können wir Sie mit unserem<br>Know-How und abgerundeten Konzept<br>unterstützen.</p>
  </div>

  <div class="abs front-text">
    <p>In regelmäßigen Abständen setzen wir uns mit Ihren<br>Mitarbeitern in Verbindung und erfragen den jeweiligen<br>IST Stand und besprechen gemeinsames Vorgehen, um<br>gesundheitliche Problematiken im Handlungsfeld Be-<br>wegung und Entspannung präventiv vorzubeugen. Ihre<br>Mitarbeiter werden dadurch in festen monatlichen Inter-<br>vallen sensibilisiert dass Sie sich um das Wohlbefinden<br>Ihrer Mitarbeiter kümmern<br>und Sie auch darin investieren.</p>
    <p class="strong">Sie als Arbeitgeber können nicht wissen und auch<br>zeitlich nicht gewährleisten welche individuellen ge-<br>sundheitlichen Problematiken Ihre Mitarbeiter haben.<br>Deshalb bieten wir Ihnen eine individuelle Lösung an<br>Dienstleistung, welche den individuellen Bedarf Ihrer<br>Mitarbeiter deckt.</p>
  </div>

  <div class="footer-tab">www.physio-lindental.de</div>
</section>

<section class="page page--back">
  <div class="abs" style="top:0;left:0;width:513px;height:131px;background:linear-gradient(90deg,#e6e2de,#bfb8b2 45%,#e8dcd6)" role="img" aria-label="Foto: Therapeutin mit Brille im Trainingsraum mit Geräten"></div>
  <div class="badge" style="left:20px;top:-7px;width:98px;height:98px">Jetzt einen<br>persönlichen<br>Termin<br>vereinbaren!</div>

  <h2 class="abs back-title">Unsere Leistungen</h2>

  <div class="col col-left">
    <h3>Messung &amp; Analysen</h3>
    <ul>
      <li>Messung &amp; Analysen zur individuellen Stress- und<br>Resilienzdiagnostik um zielorientiert ein Stress-<br>managment in Ihrem Betrieb zu implementieren.</li>
      <li>Dokumentation von Körperdaten und Risikofaktoren<br>in einer Eingangskontrolle und einem ½ jährlichen<br>Wiederholung der Kontrolle.</li>
      <li>Wirbelsäulen- und Haltungsscreenings, Haltung,<br>Beweglichkeit und Haltungskomponenten werden<br>anschaulich dargestellt und bilden die Basis für<br>zielführende Visualisierung und fundierte<br>Übungsempfehlung.</li>
      <li>Analysen von Körperstabilität und Gleichgewicht;<br>Balance-Check ist ein erprobtes Analysetool für<br>das Thema Körperstabilität</li>
    </ul>
    <h3 class="gap">Mentale Gesundheit</h3>
    <p>Programme zur Achtsamkeit, Entspannung,<br>und Wahrnehmung. In Kleingruppen, Online</p>
    <h3 class="gap">Gesundheitstage für Firmen</h3>
    <p>Individuell auf Ihre Firma abgestimmt.</p>
  </div>

  <div class="col col-right">
    <h3>Bewegungsprogramme:</h3>
    <p style="margin-bottom:4px">Präventionsprogramme nach §20 zertifiziert<br>von den Krankenkassen wie zum Beispiel:</p>
    <ul>
      <li>Entspannungskurse Hatha Yoga</li>
      <li>Pilates</li>
      <li>Rückengymnastik</li>
      <li>Ganzkörper Training an Geräten</li>
      <li>Fit am Arbeitsplatz</li>
      <li>Online-Präventionskurs<br>(zeitlich und räumlich unabhängig)</li>
      <li>und einige mehr....</li>
    </ul>
    <h3 class="gap">Digitaler Gesundheitscoach</h3>
    <ul>
      <li>Workouts</li>
      <li>Live Online- Kurse</li>
      <li>Physio Übungen gezielt und individuell<br>in der Einzelberatung online und persönlich<br>abgestimmt</li>
      <li>Online Präventionscoach<br>oder als Einzelleistung buchbar</li>
      <li>Online Präventionscoach</li>
    </ul>
  </div>

  <div class="abs cost">
    <h2>Informationen zu den Kosten</h2>
    <p>Bis zu 600 € können Sie, als Arbeitgeber steuerfrei bezuschussen.<br>Voraussetzung dafür ist, dass die fachlichen Anforderungen des<br>GKV- Spitzenverbandes erfüllt werden.</p>
    <p style="margin-top:1px">Diese Leistungen können wir erfüllen und einige mehr on Top.<br>Lassen Sie sich persönlich und individuell beraten und nehmen<br>Sie persönlich oder via E-Mail Kontakt mit uns auf.<br>Senden Sie uns eine E-Mail an hollmann@physio-lindental.de<br>und wir melden uns umgehend für eine kostenlose Beratung.</p>
  </div>

  <div class="abs contact">
    <div class="portrait" role="img" aria-label="Porträtfoto der Ansprechpartnerin"></div>
    <p class="name">Marie Hollmann</p>
    <p>Auenweg 14<br>40210 Lindental</p>
    <p>0211 - 55 60 12<br>hollmann@physio-lindental.de</p>
  </div>

  <div class="footer-tab">www.physio-lindental.de</div>
</section>

</body>
</html>
```